Car cleaning and lubrication automotive retail label

Designing a modern, trendy car cleaning and lubrication label for the retail automitive business. the label should be suitable for a retail home and garden product range. We are looking for a label that is realistic and colorful. Greens and blues are what we think would fit best for a eco label. We would like to stand out from other similar product ranges by design, meaning that we are looking for an ultra modern, simple, clean and professional design. We are also looking for a new design for the logo, clean and modern. It should include: The 'KALDRIX' logo that can have any color and "Automotive".

Example text for cleaning product (please keep in mind we need a combi cleaning product label that is also suitable for a lubrication label)

The label should have a front and a back:
Front label: Texts and slogans (in dutch):
- Reiniger, ontvetter en polisher
- Bescherming en glans
- Veilig, geconcentreerd en eco friendly
- Milieuvriendelijk
Product name: Stainless Steel Cleaner
Image of car/stainless steel on car
Eco icon
+ Icons explaining the product (cleans stainless steel on car, protection and shine, safe and concentrated, eco friendly, cleaner, degreaser, polisher)

Back label:
Instructions to use
About the product
Remarks
Updates

Target Market(s)

Automotive, car cleaning, car lubrication, car additives

Industry/Entity Type

Automotive

Colors
0692cd
a64599
e33e95
acd037
f04a50
ec1f27
cadf82
33a6d7
33b8a4

Requirements
Must have
• Must have modern colors, cool look, attract customers by an original design

```html
<!DOCTYPE html>
<html lang="nl">
<head>
<meta charset="utf-8">
<title>KALDRIX Automotive – Stainless Steel Cleaner label</title>
<link rel="stylesheet" href="https://fonts.googleapis.com/css2?family=Russo+One&family=Oswald:wght@500;600&family=Montserrat:wght@600;700;800&display=swap">
<style>
  :root{
    --page:#e6e6e6;
    --lime:#d9f24a;
    --lime-soft:#eefc9c;
    --green:#5cc12c;
    --green-deep:#2f9a22;
    --ink:#111111;
    --band:#0c0c0c;
    --title:#e8fb7a;
    --pale:#f2fdd2;
    --car-dark:#17300e;
    --car-mid:#3f7a22;
    --sky:#33a6d7;
  }
  *{margin:0;padding:0;box-sizing:border-box}
  html,body{width:1024px;height:1200px;overflow:hidden;background:var(--page)}
  .sheet{position:relative;width:1024px;height:1200px}
  .label{position:absolute;top:337px;width:470px;height:526px}
  .label--front{left:27px}
  .label--back{left:527px}
  .title{font-family:"Russo One",sans-serif;fill:var(--title);stroke:var(--ink);stroke-width:1.2;paint-order:stroke}
  .brand{font-family:"Russo One",sans-serif;fill:#123a0c}
  .brand-sub{font-family:"Montserrat",sans-serif;font-weight:800;fill:#123a0c;letter-spacing:2px}
  .tagline{font-family:"Montserrat",sans-serif;font-weight:800;fill:#ffffff;letter-spacing:1px}
  .claim{font-family:"Oswald",sans-serif;font-weight:600;fill:var(--ink)}
  .volume{font-family:"Russo One",sans-serif;fill:var(--title);stroke:var(--ink);stroke-width:1.5;paint-order:stroke}
  .eco-caption{font-family:"Montserrat",sans-serif;font-weight:800;fill:var(--ink)}
  .section-head{font-family:"Oswald",sans-serif;font-weight:500;fill:var(--ink)}
  .body-copy{font-family:"Montserrat",sans-serif;font-weight:700;fill:var(--ink);font-size:9.6px}
  .maker{font-family:"Montserrat",sans-serif;font-weight:700;fill:var(--ink);font-size:11px;letter-spacing:1px}
</style>
</head>
<body>
<main class="sheet">

  <!-- Front label -->
  <svg class="label label--front" viewBox="0 0 460 515" xmlns="http://www.w3.org/2000/svg">
    <defs>
      <clipPath id="front-shape">
        <path d="M10,95 L195,8 Q212,0 232,0 L388,4 Q422,9 440,40 L455,120 L455,492 Q455,512 435,512 L25,512 Q5,512 5,492 L5,128 Q5,106 10,95 Z"/>
      </clipPath>
      <linearGradient id="front-fill" x1="0" y1="0" x2="0.4" y2="1">
        <stop offset="0" stop-color="#c9f03c"/>
        <stop offset="0.45" stop-color="#8ad834"/>
        <stop offset="1" stop-color="#d7f23e"/>
      </linearGradient>
      <linearGradient id="car-fill" x1="0" y1="0" x2="1" y2="1">
        <stop offset="0" stop-color="var(--car-mid)"/>
        <stop offset="0.6" stop-color="var(--car-dark)"/>
        <stop offset="1" stop-color="#2a4f16"/>
      </linearGradient>
      <radialGradient id="eco-fill" cx="0.5" cy="0.5" r="0.5">
        <stop offset="0" stop-color="#7fd3f0"/>
        <stop offset="0.7" stop-color="var(--sky)"/>
        <stop offset="1" stop-color="#3fae3a"/>
      </radialGradient>
    </defs>
    <g clip-path="url(#front-shape)">
      <rect width="460" height="515" fill="url(#front-fill)"/>
      <polygon class="car-photo" role="img" aria-label="Photo of a green sports car front wheel and headlight" points="0,345 290,295 285,400 262,515 0,515" fill="url(#car-fill)"/>
      <polygon points="285,300 460,270 460,515 262,515" fill="var(--lime)"/>
      <polygon points="0,212 460,125 460,272 0,357" fill="var(--band)"/>
      <polygon points="282,318 460,286 460,328 282,358" fill="#e6f53a"/>
      <polygon points="282,368 460,336 460,380 282,410" fill="#e6f53a"/>
      <rect x="280" y="400" width="160" height="100" rx="4" fill="var(--lime-soft)" opacity="0.85"/>
    </g>

    <g class="logo" transform="rotate(-11 220 120)">
      <text class="brand" x="220" y="128" font-size="50" text-anchor="middle">KALDRIX</text>
      <text class="brand-sub" x="240" y="146" font-size="11" text-anchor="middle">AUTOMOTIVE</text>
    </g>

    <g transform="rotate(-11 225 230)">
      <text class="title" x="232" y="222" font-size="60" text-anchor="middle">STAINLESS</text>
      <text class="title" x="222" y="266" font-size="40" text-anchor="middle">STEEL CLEANER</text>
      <text class="tagline" x="205" y="290" font-size="14" text-anchor="middle">REINGER, ONVETTER EN POLISHER</text>
    </g>

    <g class="claims">
      <g transform="rotate(-10 370 330)">
        <text class="claim" x="300" y="328" font-size="12">VEILIG, GECONCENTREERD</text>
        <text class="claim" x="300" y="344" font-size="14">EN ECO FRIENDLY</text>
      </g>
      <g transform="rotate(-10 370 380)">
        <text class="claim" x="302" y="380" font-size="14">BESCHERMING</text>
        <text class="claim" x="302" y="398" font-size="18">EN GLANS</text>
      </g>
      <g class="icon-safe">
        <circle cx="272" cy="340" r="15" fill="#2a7a1c" stroke="#f4ffb0" stroke-width="2"/>
        <rect x="265" y="331" width="14" height="18" rx="2" fill="#e9f7c8"/>
        <path d="M268,337h8M268,341h8M268,345h6" stroke="#2a7a1c" stroke-width="1.5"/>
      </g>
      <g class="icon-shield">
        <circle cx="272" cy="392" r="15" fill="#4b5a66" stroke="#f4ffb0" stroke-width="2"/>
        <path d="M272,381 L282,385 L281,395 Q278,401 272,404 Q266,401 263,395 L262,385 Z" fill="#cfd8df"/>
      </g>
    </g>

    <g class="eco-badge">
      <circle role="img" aria-label="Eco icon: globe with green leaves" cx="338" cy="445" r="26" fill="url(#eco-fill)"/>
      <text class="eco-caption" x="290" y="490" font-size="8">MILIEUVRIENDELIJK</text>
    </g>

    <text class="volume" x="72" y="500" font-size="24" transform="skewX(-12) translate(105 0)">500 ml</text>
  </svg>

  <!-- Back label -->
  <svg class="label label--back" viewBox="0 0 460 515" xmlns="http://www.w3.org/2000/svg">
    <defs>
      <clipPath id="back-shape">
        <path d="M5,168 Q5,130 35,112 L280,15 Q302,6 322,6 L425,8 Q452,12 455,42 L457,485 Q457,512 430,512 L30,512 Q5,512 5,487 Z"/>
      </clipPath>
      <linearGradient id="back-fill" x1="0" y1="0" x2="0.3" y2="1">
        <stop offset="0" stop-color="#c3ee3a"/>
        <stop offset="0.55" stop-color="#8fd836"/>
        <stop offset="1" stop-color="#4fbf2e"/>
      </linearGradient>
      <radialGradient id="eco-fill-back" cx="0.5" cy="0.5" r="0.5">
        <stop offset="0" stop-color="#7fd3f0"/>
        <stop offset="0.7" stop-color="var(--sky)"/>
        <stop offset="1" stop-color="#3fae3a"/>
      </radialGradient>
    </defs>
    <g clip-path="url(#back-shape)">
      <rect width="460" height="515" fill="url(#back-fill)"/>
      <polygon points="0,0 460,0 460,98 0,182" fill="var(--band)"/>
    </g>

    <g transform="rotate(-12 215 90)">
      <text class="title" x="225" y="82" font-size="46" text-anchor="middle">STAINLESS</text>
      <text class="title" x="218" y="116" font-size="31" text-anchor="middle">STEEL CLEANER</text>
    </g>

    <g class="logo" transform="rotate(-11 355 150)">
      <text class="brand" x="355" y="158" font-size="28" text-anchor="middle">KALDRIX</text>
      <text class="brand-sub" x="362" y="168" font-size="7" text-anchor="middle">AUTOMOTIVE</text>
    </g>

    <text class="section-head" x="27" y="198" font-size="13">INSTRUCTIONS TO USE</text>
    <g class="body-copy">
      <text x="27" y="214" textLength="368" lengthAdjust="spacing">LOREM IPSUM DOLOR SIT AMET, CONSECTETUR ADIPISCING</text>
      <text x="27" y="226" textLength="368" lengthAdjust="spacing">ELIT. NULLA EST PURUS, ULTRICES IN PORTTITOR IN, AC-</text>
      <text x="27" y="238" textLength="368" lengthAdjust="spacing">CUMSAN NON QUAM. NAM CONSECTETUR PORTTITOR RHON-</text>
      <text x="27" y="250" textLength="368" lengthAdjust="spacing">CUS. CURABITUR EU EST ET LEO FEUGIAT AUCTOR VEL QUIS</text>
      <text x="27" y="262" textLength="368" lengthAdjust="spacing">LOREM. UT ET LIGULA DOLOR, SIT AMET CONSEQUAT LOREM.</text>
      <text x="27" y="274" textLength="368" lengthAdjust="spacing">ALIQUAM PORTA EROS SED VELIT IMPERDIET EGESTAS. MAE-</text>
      <text x="27" y="286" textLength="368" lengthAdjust="spacing">CENAS TEMPUS EROS UT DIAM ULLAMCORPER ID DICTUM</text>
      <text x="27" y="298" textLength="368" lengthAdjust="spacing">LIBERO TEMPOR. DONEC QUIS AUGUE QUIS MAGNA CONDI-</text>
      <text x="27" y="310" textLength="368" lengthAdjust="spacing">MENTUM LOBORTIS. QUISQUE IMPERDIET IPSUM VEL MAGNA</text>
    </g>

    <text class="section-head" x="27" y="337" font-size="13">ABOUT THE PRODUCT</text>
    <g class="body-copy">
      <text x="27" y="353" textLength="286" lengthAdjust="spacing">LOREM IPSUM DOLOR SIT AMET, CONSECTETUR</text>
      <text x="27" y="365" textLength="310" lengthAdjust="spacing">ADIPISCING ELIT. NULLA EST PURUS, ULTRICES IN</text>
      <text x="27" y="377" textLength="310" lengthAdjust="spacing">PORTTITOR IN, ACCUMSAN NON QUAM. NAM CON-</text>
      <text x="27" y="389" textLength="310" lengthAdjust="spacing">SECTETUR PORTTITOR RHONCUS. CURABITUR EU</text>
      <text x="27" y="401" textLength="310" lengthAdjust="spacing">EST ET LEO FEUGIAT AUCTOR VEL QUIS LOREM.</text>
      <text x="27" y="413" textLength="284" lengthAdjust="spacing">UT ET LIGULA DOLOR, SIT AMET CONSEQUAT</text>
      <text x="27" y="425" textLength="310" lengthAdjust="spacing">LOREM. ALIQUAM PORTA EROS SED VELIT IMPER-</text>
    </g>

    <rect class="remarks-box" x="355" y="333" width="78" height="152" fill="var(--pale)"/>

    <text class="section-head" x="52" y="449" font-size="13">MANUFACTURED BY:</text>
    <g class="maker">
      <text x="72" y="466">KALDRIX LTD</text>
      <text x="72" y="482">P.O BOX 00000</text>
      <text x="72" y="498">NETHERLANDS</text>
    </g>

    <g class="back-icons">
      <circle cx="218" cy="482" r="10" fill="#2a7a1c" stroke="#f4ffb0" stroke-width="1.5"/>
      <rect x="213" y="475" width="10" height="13" rx="1.5" fill="#e9f7c8"/>
      <circle role="img" aria-label="Eco icon: globe with green leaves" cx="258" cy="478" r="17" fill="url(#eco-fill-back)"/>
      <path d="M327,468 L336,472 L335,481 Q332,487 327,489 Q322,487 319,481 L318,472 Z" fill="#cfd8df" stroke="#4b5a66" stroke-width="1.2"/>
    </g>
  </svg>

</main>
</body>
</html>
```